Skyridge Coastal Flights
Private Jet Charter Service
Please do not use the colors pink or red...thank you.
Please do not use fighter jets on the site... we are not chartering passengers in anything like that.
Please do not try to put the logo on the plane. None of our jets have logos. Thank you!
When I open this website, the first thing I want to see is a nice jet. I don't want to see charter quoting info...I want to see attractive photos showing off jets and concierge service option...example: car services, catering on flight, hotel accommodations. I do not want the concierge service to over power the first page...maybe just a few small images? What would make you chose this charter site over the others???
Please take the charter quote box off the first page. I want to have a small link that goes to the price quote section. I do NOT want the first page looking like any of my competitors.
Hello sir,
i'm in.
HTML and CSS is not a problem but programming is another issue.... How much of the site do you want delivered after the contest is finalized?
Do you have the logo in a vector shape?
Just want to know, Do you want coding for full website or just html code for a page? if you want code for full web I can't provide them, But if just html code I will be part of this project. thanks
Hi, coding no issue. Just provide feedback. Regards
Applicant must provide coding in order to be selected.
Can you give a samples of websites that you like? how many page you want to be designed? and what if a designer isn't capable of doing the code?
Please include coding if you are capable...thank you!
I want to keep my current logo... I don't like the layout of my web page... I need something fresh.
Would it possible to upload a vector of your existing Logo? AI or EPS?

```html
<!DOCTYPE html>
<html lang="en">
<head>
<meta charset="utf-8">
<title>Skyridge Coastal Flights | Private Jet Charter Service</title>
<link href="https://fonts.googleapis.com/css2?family=Arimo:wght@400;700&display=swap" rel="stylesheet">
<style>
  :root {
    --navy-deep: #08162a;
    --navy: #0f2542;
    --navy-mid: #1b3a5f;
    --steel: #3f6d96;
    --steel-soft: #9fb8cf;
    --gold: #e8bf55;
    --paper: #ffffff;
    --paper-grey: #e6e9ed;
    --ink-grey: #7c8591;
    --title-navy: #13304f;
  }
  * { margin: 0; padding: 0; box-sizing: border-box; }
  html, body { width: 1200px; height: 996px; overflow: hidden; }
  body {
    position: relative;
    font-family: "Arimo", Arial, sans-serif;
    background:
      radial-gradient(ellipse at 20% 60%, var(--steel) 0%, transparent 45%),
      linear-gradient(135deg, var(--navy-mid) 0%, var(--navy) 45%, var(--navy-deep) 100%);
    color: var(--paper);
  }

  .site-header {
    position: absolute; left: 0; top: 0; width: 1200px; height: 156px;
    background: linear-gradient(180deg, var(--paper) 0%, var(--paper) 55%, var(--paper-grey) 100%);
  }
  .brand { position: absolute; left: 22px; top: 20px; display: flex; align-items: center; gap: 18px; }
  .brand-square { width: 64px; height: 64px; background: var(--navy); }
  .brand-name { font-size: 36px; font-weight: 700; color: var(--navy); letter-spacing: 0.5px; }
  .brand-tagline {
    position: absolute; left: 104px; top: 96px;
    font-size: 14px; font-weight: 700; letter-spacing: 2px; color: var(--ink-grey);
  }
  .header-title {
    position: absolute; right: 30px; top: 22px;
    font-size: 22px; font-weight: 700; color: var(--title-navy);
  }
  .header-contact {
    position: absolute; right: 30px; top: 58px;
    font-size: 13px; color: var(--ink-grey);
  }

  .main-nav {
    position: absolute; left: 0; top: 126px; width: 270px; height: 354px;
    background: linear-gradient(180deg, var(--navy-mid), var(--navy));
    list-style: none;
  }
  .main-nav li {
    height: 48px; display: flex; align-items: center; padding-left: 16px;
    font-size: 15px; color: var(--paper);
    border-bottom: 1px solid rgba(255,255,255,0.18);
  }
  .main-nav li::before { content: "+"; font-weight: 700; font-size: 19px; margin-right: 10px; }

  .hero-slide {
    position: absolute; left: 315px; top: 172px; width: 834px; height: 460px;
    border: 8px solid var(--paper);
    background: linear-gradient(180deg, #e3ad72 0%, #eccaa4 35%, #c9c6cc 62%, #8b8f9c 100%);
  }
  .slide-dots { position: absolute; left: 680px; top: 646px; display: flex; gap: 10px; }
  .slide-dots span { width: 18px; height: 18px; border-radius: 50%; background: var(--paper-grey); }
  .slide-dots span.active { background: var(--gold); }

  .concierge-heading {
    position: absolute; left: 317px; top: 682px;
    font-size: 21px; font-weight: 400; color: var(--gold);
  }
  .concierge-heading::before { content: "+"; color: var(--paper); font-weight: 700; margin-right: 10px; }
  .concierge-text {
    position: absolute; left: 317px; top: 724px; width: 460px;
    font-size: 14px; line-height: 19px; color: var(--paper);
  }
  .quote-link {
    position: absolute; left: 317px; top: 855px; width: 175px; height: 46px;
    background: var(--navy-mid); border: 1px solid var(--steel);
    display: flex; align-items: center; gap: 10px; padding-left: 12px;
    font-size: 14px; color: var(--paper); text-decoration: none;
  }
  .concierge-thumb {
    position: absolute; width: 153px; height: 99px; border: 4px solid var(--paper);
  }
  .thumb-car { left: 807px; top: 700px; background: linear-gradient(135deg, #c9a27a, #6b4b34); }
  .thumb-jet { left: 990px; top: 700px; background: linear-gradient(180deg, #a9c3de, #5c6670); }
  .thumb-hotel { left: 807px; top: 818px; background: linear-gradient(135deg, #f0e2cc, #8c6a4c); }
  .thumb-cabin { left: 990px; top: 818px; background: linear-gradient(135deg, #e8d6bf, #9a7a58); }

  .site-footer {
    position: absolute; left: 0; top: 942px; width: 1200px; height: 54px;
    background: var(--navy-deep);
  }
  .site-footer p { position: absolute; left: 277px; top: 16px; font-size: 13px; color: var(--paper); }
</style>
</head>
<body>
  <header class="site-header">
    <div class="brand">
      <div class="brand-square"></div>
      <span class="brand-name">Skyridge Coastal Flights</span>
    </div>
    <div class="brand-tagline">PRIVATE JET CHARTER SERVICE</div>
    <div class="header-title">Skyridge Coastal Flights | "It's a lifestyle"</div>
    <div class="header-contact">Toll Free:(800) 555-0142 | International:(602) 555-0187</div>
  </header>

  <ul class="main-nav">
    <li>HOME</li>
    <li>COMPANY</li>
    <li>PRIVATE AIRCRAFT</li>
    <li>CONCIERGE/ SERVICES</li>
    <li>SAFETY/SECURITY</li>
    <li>AIRCRAFT MANAGEMENT</li>
    <li>CONTACT US</li>
  </ul>

  <div class="hero-slide" role="img" aria-label="Private business jet flying above sunset clouds"></div>
  <div class="slide-dots"><span class="active"></span><span></span><span></span><span></span><span></span></div>

  <h2 class="concierge-heading">Concierge for Aircraft Charter Services</h2>
  <p class="concierge-text">One stop trip planner including: Charter Flight, hotel accommodations, limo, rental car, aircraft catering. Special Aircraft Chartering request like birthday cakes, flowers and more. Request reading material such as magazines, newspapers, books, etc.</p>

  <a class="quote-link" href="#quote">
    <svg width="26" height="20" viewBox="0 0 26 20" aria-hidden="true">
      <path d="M1 11 L25 3 L18 10 L25 17 Z" fill="#ffffff"/>
    </svg>
    Quotation Request
  </a>

  <div class="concierge-thumb thumb-car" role="img" aria-label="Luxury car service interior"></div>
  <div class="concierge-thumb thumb-jet" role="img" aria-label="Jet parked on the runway"></div>
  <div class="concierge-thumb thumb-hotel" role="img" aria-label="Hotel accommodation suite"></div>
  <div class="concierge-thumb thumb-cabin" role="img" aria-label="Jet cabin with catering"></div>

  <footer class="site-footer">
    <p>Copyright© 2009-2011, All Rights Reserved skyridgecoastalflights.com</p>
  </footer>
</body>
</html>
```